Launching a new real estate agency in Monaco

Hello, I am opening a new real estate agency in Monaco. For the purpose of my activity, in order to be known quickly among a fierce competition I need an advertising campaign that will be broadcast in local magazines, newspapers, paper board, etc.

You will find example of pictures of Monaco on which I have the rights and my logo. You can always pick other images that I can buy if the price is reasonable for a commercial use (<200 $)

Please respect the color code.

I wish you good luck and look forward to give you my feedbacks

Reason: Only few projects posted were respecting the brief and of quality. Hoping to receive more in coming days

Target Market(s)

International high-end clientele of all ages, all genders.

Industry/Entity Type

Real Estate Agent

Font styles to use
Serif

Requirements
Must have
• 1/ My logo
• 2/ This message "Un nouveau regard sur l'immobilier" means in English a fresh look at real estate or new eyes on real-estate.
• 3/ My address: 14 rue des Orvilles, Passage Marcellin, 98 000 Monaco
• 4/ Phone number: +377.93.48.25.71
• 5/ Website: www.brunor-agency.com.
• 6/ Format: Files should be easily adjustable but I'd like a vertical display to fit easily in Magazines, Poster and billboard. So please work in high resolution !
Nice to have
• Please think about your design in accordance with the message I want to display.
Should not have
• A simple poster with a picture of Monaco that does not take into consideration the message of the advertisement, "Un nouveau regard sur l'immobilier" which means in english, new eyes on real-estate or a new look at real-estate, or new vision at real-estate.

```html
<!DOCTYPE html>
<html lang="fr">
<head>
<meta charset="utf-8">
<title>Brunor Agency — Un nouveau regard sur l'immobilier</title>
<link rel="stylesheet" href="https://fonts.googleapis.com/css2?family=Playfair+Display:wght@900&family=Arimo:wght@400;700&display=swap">
<style>
  :root {
    --backdrop: #e4e2df;
    --paper: #ffffff;
    --ink-black: #000000;
    --navy: #243a5a;
    --copper: #c4866a;
    --sea-deep: #1f4fa8;
    --sea-light: #3f78c9;
    --city-warm: #d98f6c;
    --city-pale: #e8d9cf;
  }
  * { margin: 0; padding: 0; box-sizing: border-box; }
  html, body {
    width: 1200px; height: 1200px; overflow: hidden;
    background: var(--backdrop);
  }
  .poster {
    position: absolute;
    left: 226px; top: 40px;
    width: 748px; height: 1120px;
    background: var(--paper);
    overflow: hidden;
  }
  .poster__viewer {
    position: absolute; left: 0; top: 0;
    width: 748px; height: 600px;
    display: block;
  }
  .poster__headline {
    position: absolute; left: 0; top: 640px; width: 100%;
    text-align: center;
    font-family: "Playfair Display", serif;
    font-weight: 900;
    font-size: 80px;
    line-height: 80px;
    letter-spacing: 1px;
    color: var(--navy);
    text-transform: uppercase;
  }
  .brand {
    position: absolute; left: 0; top: 962px; width: 100%;
    display: flex; justify-content: center; align-items: center; gap: 12px;
  }
  .brand__mark {
    width: 22px; height: 22px; background: var(--copper);
  }
  .brand__name {
    font-family: "Playfair Display", serif;
    font-weight: 900;
    font-size: 30px;
    letter-spacing: 2px;
    color: var(--copper);
    text-transform: uppercase;
  }
  .contact {
    position: absolute; left: 0; width: 100%;
    text-align: center;
    font-family: "Arimo", sans-serif;
    color: var(--navy);
  }
  .contact--address { top: 1030px; font-size: 17px; }
  .contact--lines {
    top: 1063px; font-size: 16px;
    display: flex; justify-content: center; gap: 30px;
  }
  .contact__item { display: flex; align-items: center; gap: 14px; }
  .contact__icon { width: 16px; height: 16px; fill: var(--navy); }
</style>
</head>
<body>
  <main class="poster">
    <svg class="poster__viewer" viewBox="0 0 748 600" aria-hidden="false">
      <defs>
        <linearGradient id="harbourTones" x1="0" y1="0" x2="0" y2="1">
          <stop offset="0" stop-color="var(--sea-deep)"/>
          <stop offset="0.35" stop-color="var(--sea-light)"/>
          <stop offset="0.6" stop-color="var(--city-pale)"/>
          <stop offset="1" stop-color="var(--city-warm)"/>
        </linearGradient>
      </defs>
      <rect x="0" y="0" width="748" height="342" fill="var(--ink-black)"/>
      <circle cx="201" cy="342" r="235" fill="var(--ink-black)"/>
      <circle cx="547" cy="342" r="235" fill="var(--ink-black)"/>
      <g role="img" aria-label="Aerial photograph of the Monaco harbour with yachts and city buildings, seen through binoculars">
        <ellipse cx="201" cy="342" rx="173" ry="171" fill="url(#harbourTones)"/>
        <ellipse cx="547" cy="342" rx="173" ry="171" fill="url(#harbourTones)"/>
      </g>
    </svg>

    <h1 class="poster__headline">Un nouveau<br>regard sur<br>l'immobilier</h1>

    <div class="brand">
      <span class="brand__mark"></span>
      <span class="brand__name">Brunor Agency</span>
    </div>

    <p class="contact contact--address">14 rue des Orvilles, Passage Marcellin, 98 000 Monaco</p>
    <div class="contact contact--lines">
      <span class="contact__item">
        <svg class="contact__icon" viewBox="0 0 24 24"><path d="M6.6 10.8a15.1 15.1 0 0 0 6.6 6.6l2.2-2.2c.3-.3.7-.4 1-.2 1.1.4 2.3.6 3.6.6.6 0 1 .4 1 1V20c0 .6-.4 1-1 1A17 17 0 0 1 3 4c0-.6.4-1 1-1h3.5c.6 0 1 .4 1 1 0 1.3.2 2.5.6 3.6.1.3 0 .7-.2 1z"/></svg>
        +377.93.48.25.71
      </span>
      <span class="contact__item">
        <svg class="contact__icon" viewBox="0 0 24 24"><path d="M12 2a10 10 0 1 0 0 20 10 10 0 0 0 0-20zm6.9 6h-2.9a15.6 15.6 0 0 0-1.4-3.6A8 8 0 0 1 18.9 8zM12 4c.8 1.2 1.5 2.5 1.9 4h-3.8c.4-1.4 1.1-2.8 1.9-4zM4.3 14a8.2 8.2 0 0 1 0-4h3.4a16.5 16.5 0 0 0 0 4zm.8 2h2.9c.3 1.3.8 2.5 1.4 3.6A8 8 0 0 1 5.1 16zM8 8H5.1a8 8 0 0 1 4.3-3.6C8.8 5.5 8.3 6.7 8 8zm4 12c-.8-1.2-1.5-2.5-1.9-4h3.8c-.4 1.4-1.1 2.8-1.9 4zm2.3-6H9.7a14.7 14.7 0 0 1 0-4h4.6a14.7 14.7 0 0 1 0 4zm.3 5.6c.6-1.1 1.1-2.3 1.4-3.6h2.9a8 8 0 0 1-4.3 3.6zm1.7-5.6a16.5 16.5 0 0 0 0-4h3.4a8.2 8.2 0 0 1 0 4z"/></svg>
        www.brunor-agency.com
      </span>
    </div>
  </main>
</body>
</html>
```